Mental Health & Addiction Podcast Art

Project: Podcast Cover Art / Visual Identity
Podcast Name: The Renewal Compass
Focus: Recovery from substance use and mental health
Objectives
Create compelling podcast artwork that:
Reflects the themes of hope, healing, and personal growth
Establishes credibility and professionalism
Appeals to individuals seeking recovery resources and support
Maintains strong brand consistency with Harborline Wellness
Brand Integration Requirements
Logo incorporation: Integrate an element from the Harborline Wellness Logo—potentially an abstract or partial use of the sun motif
Flexibility: Open to creative interpretations (e.g., sun rays as background texture, sunrise gradient, partial sun as a design accent)
Mandatory: Must adhere to existing Harborline Wellness brand guidelines (approved color palette, typography, and visual style)

Target Market(s)

United states, people with addiction and mental health disorders.

Industry/Entity Type

Wellness

Font styles to use
Other font styles liked:
• See Brand Guide

Requirements
Must have
• Match brand guide, in corporate elements of the Harborline Wellness Logo icon

```html
<!DOCTYPE html>
<html lang="en">
<head>
<meta charset="utf-8">
<title>The Renewal Compass — Podcast Cover</title>
<link href="https://fonts.googleapis.com/css2?family=Playfair+Display:wght@700;800&display=swap" rel="stylesheet">
<style>
  :root {
    --ink: #000000;
    --white: #ffffff;
    --gold: #ffb400;
    --gold-deep: #f7a600;
    --gold-light: #fff3c4;
    --glow-core: #fffbe8;
    --glow-mid: #f3b53a;
    --glow-edge: #6a3f06;
  }
  html, body {
    margin: 0;
    padding: 0;
    width: 1200px;
    height: 1200px;
    overflow: hidden;
    background: var(--ink);
  }
  .cover {
    position: relative;
    width: 1200px;
    height: 1200px;
    background: var(--ink);
    overflow: hidden;
    font-family: "Playfair Display", Georgia, serif;
  }
  .sunburst {
    position: absolute;
    inset: 0;
    background:
      radial-gradient(circle at 984px 316px, var(--glow-core) 0, #fff2b0 40px, #ffd560 90px, var(--glow-mid) 180px, rgba(180,110,20,0.75) 330px, rgba(106,63,6,0.45) 520px, rgba(40,22,2,0.15) 700px, rgba(0,0,0,0) 860px);
  }
  .brand {
    position: absolute;
    left: 90px;
    top: 262px;
    display: flex;
    align-items: center;
    gap: 16px;
    color: var(--white);
    font-weight: 700;
    font-size: 26px;
    letter-spacing: 3px;
    line-height: 1.25;
  }
  .brand-dot {
    width: 44px;
    height: 44px;
    border-radius: 50%;
    background: var(--gold);
    flex: none;
  }
  .title {
    position: absolute;
    left: 88px;
    top: 498px;
    margin: 0;
    font-weight: 700;
    font-size: 146px;
    line-height: 136px;
    letter-spacing: -1px;
  }
  .title-lead {
    display: block;
    color: var(--white);
  }
  .title-accent {
    display: block;
    background: linear-gradient(90deg, var(--gold-deep) 0%, var(--gold) 55%, var(--gold-light) 100%);
    -webkit-background-clip: text;
    background-clip: text;
    color: transparent;
    width: max-content;
  }
  .format-label {
    position: absolute;
    left: 94px;
    top: 988px;
    color: var(--white);
    font-weight: 700;
    font-size: 38px;
    letter-spacing: 32px;
  }
</style>
</head>
<body>
  <main class="cover">
    <div class="sunburst" role="img" aria-label="Golden sunburst of radiating light rays glowing from the upper right"></div>

    <div class="brand">
      <span class="brand-dot"></span>
      <span class="brand-name">HARBORLINE<br>WELLNESS</span>
    </div>

    <h1 class="title">
      <span class="title-lead">THE</span>
      <span class="title-accent">RENEWAL</span>
      <span class="title-accent">COMPASS</span>
    </h1>

    <div class="format-label">PODCAST</div>
  </main>
</body>
</html>
```